Uni Camp Poster (Theme: Desert Oasis)

We require a poster design for our annual camp with the theme "desert oasis", please see the attached design brief for details.
We are the Coralline Fellowship (Cf), founded in 1996 at the Wexbridge Institute of Learning. As one of the largest social clubs at the Wexbridge Institute of Learning, Cf runs a variety of premier social and sporting events for University students.
Target Market(s)
18-19 year olds in Melbourne

```html
<!DOCTYPE html>
<html lang="en">
<head>
<meta charset="UTF-8">
<title>Oasis – Annual Camp 2022</title>
<link rel="stylesheet" href="https://fonts.googleapis.com/css2?family=Playfair+Display:ital,wght@0,700;0,800;1,700&family=Poppins:ital,wght@0,600;1,300&display=swap">
<style>
  :root {
    --sky-top: #1f5fa8;
    --sky-low: #8fb6d6;
    --sand-far: #e7a93a;
    --sand-mid: #c97f1d;
    --palm: #4a4a1e;
    --lake: #123a6a;
    --sand-near: #d99530;
    --sand-deep: #8a4a12;
    --gold-light: #ffd65a;
    --gold: #f3b61f;
    --gold-deep: #d9921a;
    --cream: #fffaf0;
    --backdrop: #2a2a2a;
  }
  * { margin: 0; padding: 0; box-sizing: border-box; }
  html, body {
    width: 1200px; height: 675px; overflow: hidden;
    background: var(--backdrop);
  }
  .poster {
    position: relative;
    width: 1200px; height: 675px;
    overflow: hidden;
  }
  .scene-photo {
    position: absolute; inset: 0;
    background: linear-gradient(180deg,
      var(--sky-top) 0%,
      #3a7bc0 22%,
      var(--sky-low) 37%,
      var(--sand-far) 40%,
      var(--sand-mid) 52%,
      var(--palm) 56%,
      var(--lake) 60%,
      var(--lake) 70%,
      var(--palm) 74%,
      var(--sand-near) 80%,
      var(--sand-deep) 100%);
  }
  .title {
    position: absolute;
    left: 92px; top: 40px;
    font-family: "Playfair Display", serif;
    font-weight: 800;
    font-size: 196px;
    line-height: 1;
    letter-spacing: -4px;
    background: linear-gradient(180deg, var(--gold-light), var(--gold) 55%, var(--gold-deep));
    -webkit-background-clip: text;
    background-clip: text;
    color: transparent;
    filter: drop-shadow(2px 3px 3px rgba(0,0,0,0.35));
  }
  .subtitle {
    position: absolute;
    left: 614px; top: 172px;
    font-family: "Playfair Display", serif;
    font-weight: 700;
    font-size: 35px;
    letter-spacing: -0.5px;
    color: var(--gold);
    text-shadow: 1px 2px 2px rgba(0,0,0,0.4);
    white-space: nowrap;
  }
  .club-mark {
    position: absolute;
    right: 33px; top: 30px;
    display: flex; align-items: center; gap: 10px;
  }
  .club-mark__dot {
    width: 30px; height: 30px; border-radius: 50%;
    border: 3px solid var(--gold);
  }
  .club-mark__name {
    font-family: "Poppins", sans-serif;
    font-weight: 600;
    font-size: 19px;
    line-height: 1.05;
    text-transform: uppercase;
    color: var(--gold);
  }
  .event-name {
    position: absolute;
    left: 37px; top: 560px;
    font-family: "Playfair Display", serif;
    font-weight: 700;
    font-size: 46px;
    line-height: 1;
    color: var(--cream);
    text-shadow: 1px 2px 3px rgba(0,0,0,0.4);
  }
  .pricing {
    position: absolute;
    left: 53px; top: 611px;
    font-family: "Poppins", sans-serif;
    font-style: italic;
    font-weight: 300;
    font-size: 21px;
    color: var(--gold-light);
  }
  .union-mark {
    position: absolute;
    right: 32px; top: 595px;
    font-family: "Poppins", sans-serif;
    font-weight: 600;
    font-size: 44px;
    line-height: 1;
    color: var(--cream);
  }
</style>
</head>
<body>
  <main class="poster">
    <div class="scene-photo" role="img" aria-label="Photograph of golden desert dunes under a blue sky with clouds, surrounding a deep blue oasis lake ringed by palm trees"></div>

    <h1 class="title">Oasis</h1>
    <p class="subtitle">A Journey through the Sands</p>

    <div class="club-mark">
      <span class="club-mark__dot"></span>
      <span class="club-mark__name">Coralline<br>Fellowship</span>
    </div>

    <h2 class="event-name">Annual camp 2022</h2>
    <p class="pricing">$155 for Members and $165 for Non-Members</p>

    <div class="union-mark">WISU</div>
  </main>
</body>
</html>
```